Stationary and document suite for consultancy business in Australia called Lumeta

I would like to get a suite of documents suitable for my new business called Lumeta. I have included the original brief below, however have already selected a design for the logo. I would like to get:
Letter head - simple letter template with "V" logo embossed in background
Word document - standard format with "V" logo embossed in background
Proposal document - bolder pages with cover and back cover, include empty pages with footer as well as contents
Powerpoint presentation - open to ideas
Email signature - banner style or text, open to ideas
Brief that was given for logo (logo not required)
The name of the business is derived from the latin word for green ("Viridis") combined with "co" which is intended to represent a number of different words: collaborative, cooperative, coaching, collective,  construction, consulting, etc.
My objective for the brand is to represent a dynamic, progressive and collaborative business, where our people have fun and enjoy their work.
The objective of our business is to provide consultancy services to construction businesses, mainly aimed at building high performing teams and strategic growth. We will create learning and development tools that businesses can use to increase staff satisfaction and retention. Our future goal is to invest in decarbonisation and sustainability technology for use in the construction industry.
Our target market is construction business leaders and infrastructure owners, who operate road, rail and utility assets. We also want to present as a dynamic, progressive and fun place to work that will be attractive to new employees.

```html
<!DOCTYPE html>
<html lang="en">
<head>
<meta charset="utf-8">
<title>Lumeta stationery suite</title>
<link href="https://fonts.googleapis.com/css2?family=Roboto:wght@400;500;700&family=Poppins:wght@500;600&display=swap" rel="stylesheet">
<style>
:root{
  --green:#7dc242;
  --grey:#6d6e70;
  --dark:#333436;
  --text:#55575a;
  --line:#9a9b9d;
  --photo:#4a4648;
  --bg-top:#e6e7e9;
  --bg-bottom:#d8d9db;
  --paper:#ffffff;
}
*{margin:0;padding:0;box-sizing:border-box}
html,body{width:1200px;height:2956px;overflow:hidden}
body{position:relative;font-family:"Roboto",Arial,sans-serif;color:var(--text);background:var(--bg-bottom)}
.band-top{position:absolute;left:0;top:0;width:1200px;height:1248px;background:var(--bg-top)}
.sheet{position:absolute;background:var(--paper)}
.wordmark{font-family:"Roboto",Arial,sans-serif;font-weight:500;color:var(--grey);display:flex;align-items:center;gap:.3em;letter-spacing:.02em}
.wordmark .dot{width:.42em;height:.42em;border-radius:50%;background:var(--green)}

/* letterhead */
.letterhead{left:228px;top:174px;width:642px;height:894px}
.letterhead .wordmark{position:absolute;left:0;right:0;top:238px;justify-content:center;font-size:50px}
.letter-body{position:absolute;left:55px;top:222px;width:527px;font-size:11.4px;line-height:17.4px;color:var(--text)}
.letter-body p{text-align:justify;margin-bottom:17.4px}
.signature{position:absolute;left:58px;top:666px;width:74px;height:72px;background:#eef0f4;border-radius:4px}
.letter-footer{position:absolute;left:55px;top:836px;width:527px;display:flex;justify-content:space-between;font-size:15.5px;color:var(--dark)}
.contact{display:flex;align-items:center;gap:4px}
.ico{width:1em;height:1em;flex:none}

/* slides */
.slide{width:388px;height:294px;overflow:hidden}
.s1{left:196px;top:1357px}.s2{left:617px;top:1357px}
.s3{left:196px;top:1684px}.s4{left:617px;top:1684px}
.s5{left:196px;top:2011px}.s6{left:617px;top:2011px;background:var(--green)}
.slide-head{position:absolute;left:26px;top:40px;width:336px}
.slide-head h2{font-size:15.6px;font-weight:700;color:var(--green);line-height:1}
.slide-head .sub{display:flex;align-items:center;gap:4px;font-size:8.5px;color:var(--dark);margin-top:2px}
.slide-head .sub::after{content:"";flex:1;height:1px;background:var(--line)}
.slide .corner{position:absolute;right:26px;top:24px;font-size:16px}
.tiny{font-size:4.6px;line-height:6.4px;color:#77797c;text-align:justify}
.cover{position:absolute;left:0;right:0;text-align:center;font-family:"Poppins",sans-serif}
.s1 .wordmark{position:absolute;left:0;right:0;top:110px;justify-content:center;font-size:46px}
.welcome{top:194px;font-size:14.4px;font-weight:500;color:var(--dark)}
.pres{top:214px;font-size:20px;font-weight:600;color:var(--green)}
.desc{top:240px;font-size:14.4px;font-weight:500;color:var(--dark)}

.team{position:absolute;left:26px;top:98px;display:flex;gap:9px}
.member{width:77px}
.photo{width:77px;height:79px;background:var(--photo);display:flex;align-items:center;justify-content:center;color:#fff;font-size:9px;font-weight:500}
.member .name{margin-top:12px;font-size:9.5px;color:var(--green);line-height:1}
.member .role{font-size:8.5px;color:var(--grey);margin-bottom:8px;line-height:1.2}

.groups{position:absolute;left:26px;top:90px;width:336px;display:grid;grid-template-columns:162px 162px;column-gap:14px;row-gap:12px}
.group h3{font-size:6px;color:var(--green);font-weight:700;margin-bottom:3px}

.chart{position:absolute;left:26px;top:100px}
.s4 .tiny{position:absolute;left:20px;top:214px;width:348px}

.s5 .left-text{position:absolute;left:26px;top:90px;width:160px}
.pie{position:absolute;left:208px;top:72px}
.s5 .bottom{position:absolute;left:26px;top:210px;width:336px;display:grid;grid-template-columns:160px 160px;gap:16px}

.thanks{position:absolute;left:0;right:0;top:68px;text-align:center;color:#fff;font-family:"Poppins",sans-serif;font-weight:500;font-size:40px;line-height:48px}
.thanks-contact{position:absolute;left:0;right:0;top:222px;text-align:center;color:#fff;font-size:9px;line-height:13px}

/* business card */
.card{left:286px;top:2579px;width:628px;height:230px}
.card .name{position:absolute;left:42px;top:36px;font-size:22px;font-weight:700;color:var(--dark);letter-spacing:.01em}
.card .title{position:absolute;left:42px;top:62px;font-size:19px;color:var(--green)}
.card-contacts{position:absolute;left:42px;top:120px;font-size:18px;color:var(--dark);line-height:25.5px}
.card .wordmark{position:absolute;left:360px;top:132px;font-size:50px}
</style>
</head>
<body>
<div class="band-top"></div>

<section class="sheet letterhead">
  <div class="wordmark" style="top:54px"><span>Lumeta</span><span class="dot"></span></div>
  <div class="letter-body">
    <p style="margin-bottom:16px">Dear customer,</p>
    <p>Lorem ipsum dolor sit amet, consectetur adipisicing elit, sed do eiusmod tempor incididunt ut labore et dolore magna aliqua. Ut enim ad minim veniam, quis nostrud exercitation ullamco laboris nisi ut aliquip ex ea commodo consequat. Duis aute irure dolor in reprehenderit in voluptate velit esse cillum dolore eu fugiat nulla pariatur. Excepteur sint occaecat cupidatat non proident, sunt in culpa qui officia deserunt mollit anim id est laborum.</p>
    <p>Lorem ipsum dolor sit amet, consectetur adipisicing elit, sed do eiusmod tempor incididunt ut labore et dolore magna aliqua. Ut enim ad minim veniam, quis nostrud exercitation ullamco laboris nisi ut aliquip ex ea commodo consequat. Duis aute irure dolor in reprehenderit in voluptate velit esse cillum dolore eu fugiat nulla pariatur. Excepteur sint occaecat cupidatat non proident, sunt in culpa qui officia deserunt mollit anim id est laborum.</p>
    <p>Lorem ipsum dolor sit amet, consectetur adipisicing elit, sed do eiusmod tempor incididunt ut labore et dolore magna aliqua. Ut enim ad minim veniam, quis nostrud exercitation ullamco laboris nisi ut aliquip ex ea commodo consequat. Duis aute irure dolor in reprehenderit in voluptate velit esse cillum dolore eu fugiat nulla pariatur. Excepteur sint occaecat cupidatat non proident, sunt in culpa qui officia deserunt mollit anim id est laborum.</p>
    <p>Lorem ipsum dolor sit amet, consectetur adipisicing elit, sed do eiusmod tempor incididunt ut labore et dolore magna aliqua. Ut enim ad minim veniam, quis nostrud exercitation ullamco laboris nisi ut aliquip ex ea commodo consequat. Duis aute irure dolor in reprehenderit.</p>
    <p>Yours Sincerely,</p>
  </div>
  <div class="signature" role="img" aria-label="Handwritten signature"></div>
  <div class="letter-footer">
    <span class="contact"><svg class="ico" viewBox="0 0 16 16"><circle cx="8" cy="8" r="8" fill="#7dc242"/><path d="M5 4.5l1.5-.3 1 2-1 .8a5 5 0 0 0 2.5 2.5l.8-1 2 1-.3 1.5c-3.5.3-6.8-3-6.5-6.5z" fill="#fff"/></svg>+61 400 512 873</span>
    <span class="contact"><svg class="ico" viewBox="0 0 16 16"><circle cx="8" cy="8" r="8" fill="#7dc242"/><rect x="4" y="5" width="8" height="6" rx="1" fill="none" stroke="#fff" stroke-width="1.2"/><path d="M4 5.5l4 3 4-3" fill="none" stroke="#fff" stroke-width="1.2"/></svg>marcus@lumeta.com.au</span>
    <span class="contact"><svg class="ico" viewBox="0 0 16 16"><circle cx="8" cy="8" r="8" fill="#7dc242"/><circle cx="8" cy="8" r="4" fill="none" stroke="#fff" stroke-width="1.2"/><path d="M4 8h8M8 4c-2 2.5-2 5.5 0 8M8 4c2 2.5 2 5.5 0 8" fill="none" stroke="#fff" stroke-width=".9"/></svg>www.lumeta.com.au</span>
  </div>
</section>

<!-- presentation slides -->
<section class="sheet slide s1">
  <div class="wordmark"><span>Lumeta</span><span class="dot"></span></div>
  <p class="cover welcome">Welcome to Our</p>
  <p class="cover pres">Presentation Name</p>
  <p class="cover desc">Description</p>
</section>

<section class="sheet slide s2">
  <div class="wordmark corner"><span>Lumeta</span><span class="dot"></span></div>
  <div class="slide-head"><h2>Heading Here</h2><div class="sub">Sub Heading</div></div>
  <div class="team">
    <div class="member"><div class="photo" role="img" aria-label="Team member photo">Photo</div><p class="name">Team Member1</p><p class="role">Title</p><p class="tiny">Short profile of the team member and role.</p></div>
    <div class="member"><div class="photo" role="img" aria-label="Team member photo">Photo</div><p class="name">Team Member1</p><p class="role">Title</p><p class="tiny">Short profile of the team member and role.</p></div>
    <div class="member"><div class="photo" role="img" aria-label="Team member photo">Photo</div><p class="name">Team Member1</p><p class="role">Title</p><p class="tiny">Short profile of the team member and role.</p></div>
    <div class="member"><div class="photo" role="img" aria-label="Team member photo">Photo</div><p class="name">Team Member1</p><p class="role">Title</p><p class="tiny">Short profile of the team member and role.</p></div>
  </div>
</section>

<section class="sheet slide s3">
  <div class="wordmark corner"><span>Lumeta</span><span class="dot"></span></div>
  <div class="slide-head"><h2>Heading Here</h2><div class="sub">Sub Heading</div></div>
  <div class="groups">
    <div class="group"><h3>Group 1</h3><p class="tiny">Brief notes describing this group, its aims and the key actions planned.</p></div>
    <div class="group"><h3>Group 1</h3><p class="tiny">Brief notes describing this group, its aims and the key actions planned.</p></div>
    <div class="group"><h3>Group 1</h3><p class="tiny">Brief notes describing this group, its aims and the key actions planned.</p></div>
    <div class="group"><h3>Group 1</h3><p class="tiny">Brief notes describing this group, its aims and the key actions planned.</p></div>
    <div class="group"><h3>Group 1</h3><p class="tiny">Brief notes describing this group, its aims and the key actions planned.</p></div>
    <div class="group"><h3>Group 1</h3><p class="tiny">Brief notes describing this group, its aims and the key actions planned.</p></div>
  </div>
</section>

<section class="sheet slide s4">
  <div class="wordmark corner"><span>Lumeta</span><span class="dot"></span></div>
  <div class="slide-head"><h2>Heading Here</h2><div class="sub">Sub Heading</div></div>
  <svg class="chart" width="336" height="100" viewBox="0 0 336 100" font-family="Roboto,sans-serif" font-size="4" fill="#8a8c8f">
    <g stroke="#e3e4e5" stroke-width=".6"><line x1="10" y1="8" x2="330" y2="8"/><line x1="10" y1="22" x2="330" y2="22"/><line x1="10" y1="36" x2="330" y2="36"/><line x1="10" y1="50" x2="330" y2="50"/><line x1="10" y1="64" x2="330" y2="64"/></g>
    <g fill="#7dc242"><rect x="22" y="14" width="10" height="50"/><rect x="58" y="22" width="10" height="42"/><rect x="98" y="30" width="10" height="34"/><rect x="112" y="12" width="10" height="52"/><rect x="176" y="30" width="10" height="34"/><rect x="204" y="18" width="10" height="46"/><rect x="250" y="20" width="10" height="44"/><rect x="264" y="10" width="10" height="54"/><rect x="278" y="14" width="10" height="50"/></g>
    <g fill="#8a8c8f"><rect x="36" y="42" width="10" height="22"/><rect x="176" y="42" width="0" height="0"/><rect x="190" y="46" width="10" height="18"/><rect x="250" y="20" width="0" height="0"/><rect x="236" y="36" width="10" height="28"/></g>
    <g fill="#2b2d30"><rect x="46" y="40" width="10" height="24"/><rect x="126" y="40" width="10" height="24"/></g>
    <g fill="#7dc242"><rect x="140" y="32" width="10" height="32"/></g>
    <line x1="10" y1="64" x2="330" y2="64" stroke="#bbb" stroke-width=".6"/>
    <text x="44" y="72">2019</text><text x="120" y="72">2020</text><text x="196" y="72">2021</text><text x="266" y="72">2022</text>
    <g><rect x="30" y="83" width="3" height="3" fill="#7dc242"/><text x="35" y="86">Series A</text><rect x="75" y="83" width="3" height="3" fill="#7dc242"/><text x="80" y="86">Series B</text><rect x="120" y="83" width="3" height="3" fill="#2b2d30"/><text x="125" y="86">Series C</text><rect x="165" y="83" width="3" height="3" fill="#8a8c8f"/><text x="170" y="86">Series D</text></g>
  </svg>
  <p class="tiny">Revenue grew steadily across each year, with strong results from advisory work and team programs. Growth in training and coaching lifted returns, while project costs held stable. The outlook remains positive as new clients join and delivery capacity expands across regions.</p>
</section>

<section class="sheet slide s5">
  <div class="wordmark corner"><span>Lumeta</span><span class="dot"></span></div>
  <div class="slide-head"><h2>Heading Here</h2><div class="sub">Sub Heading</div></div>
  <p class="tiny left-text">Our yearly results show how income is shared across sales, revenue, profit and spending. Most value came from consulting programs delivered to construction teams. Spending stayed within plan while profit rose, giving room to invest in new tools, coaching and sustainability research over the coming year.</p>
  <svg class="pie" width="160" height="130" viewBox="-80 -60 160 130" font-family="Roboto,sans-serif" font-size="4.5">
    <path d="M0 0L0-50A50 50 0 0 1 48.4-12.4Z" fill="#a3a59a"/>
    <path d="M0 0L48.4-12.4A50 50 0 0 1 29.4 40.5Z" fill="#23262a"/>
    <path d="M0 0L29.4 40.5A50 50 0 1 1 0-50Z" fill="#7dc242"/>
    <text x="10" y="-36" fill="#fff">21%</text><text x="32" y="2" fill="#fff">19%</text><text x="-28" y="26" fill="#fff">60%</text>
    <g fill="#333"><rect x="-68" y="63" width="3" height="3" fill="#7dc242"/><text x="-63" y="66">Sale</text><rect x="-48" y="63" width="3" height="3" fill="#7dc242"/><text x="-43" y="66">Revenue</text><rect x="-18" y="63" width="3" height="3" fill="#23262a"/><text x="-13" y="66">Profit</text><rect x="6" y="63" width="3" height="3" fill="#23262a"/><text x="11" y="66">Expenditure</text></g>
  </svg>
  <div class="bottom">
    <p class="tiny">Sales remain the largest share, driven by repeat clients and new leadership programs.</p>
    <p class="tiny">Sales remain the largest share, driven by repeat clients and new leadership programs.</p>
  </div>
</section>

<section class="sheet slide s6">
  <p class="thanks">Thanks<br>For Wathing</p>
  <p class="thanks-contact">P : +61 400 512 873 E : marcus@lumeta.com.au<br>14 Harbour Lane, Carlton, VIC 3053<br>www.lumeta.com.au</p>
</section>

<!-- business card -->
<section class="sheet card">
  <p class="name">MARCUS ELLERY</p>
  <p class="title">Director</p>
  <div class="card-contacts">
    <p class="contact"><svg class="ico" viewBox="0 0 16 16"><circle cx="8" cy="8" r="8" fill="#7dc242"/><path d="M5 4.5l1.5-.3 1 2-1 .8a5 5 0 0 0 2.5 2.5l.8-1 2 1-.3 1.5c-3.5.3-6.8-3-6.5-6.5z" fill="#fff"/></svg>+61 400 512 873</p>
    <p class="contact"><svg class="ico" viewBox="0 0 16 16"><circle cx="8" cy="8" r="8" fill="#7dc242"/><rect x="4" y="5" width="8" height="6" rx="1" fill="none" stroke="#fff" stroke-width="1.2"/><path d="M4 5.5l4 3 4-3" fill="none" stroke="#fff" stroke-width="1.2"/></svg>marcus@lumeta.com.au</p>
    <p class="contact"><svg class="ico" viewBox="0 0 16 16"><circle cx="8" cy="8" r="8" fill="#7dc242"/><circle cx="8" cy="8" r="4" fill="none" stroke="#fff" stroke-width="1.2"/><path d="M4 8h8M8 4c-2 2.5-2 5.5 0 8M8 4c2 2.5 2 5.5 0 8" fill="none" stroke="#fff" stroke-width=".9"/></svg>lumeta.com.au</p>
  </div>
  <div class="wordmark"><span>Lumeta</span><span class="dot"></span></div>
</section>
</body>
</html>
```